Asset tracing and investigation firm requires marketing brochure for services

We need a professional looking brochure with layout that supports the text that we have already drafted, is easy on the eye and can easily be navigated by clients either electronic/screen format or printed format. The wording is not finalised and all aspects need to be remain editable (including the logo and picture(s)) - preferably in Word or similarly accessible format.

```html
<!DOCTYPE html>
<html lang="en">
<head>
<meta charset="utf-8">
<title>Orvane Asset Tracing Services – Brochure Cover</title>
<link rel="stylesheet" href="https://fonts.googleapis.com/css2?family=Montserrat:wght@400;600;700&family=Cinzel:wght@500&display=swap">
<style>
  :root {
    --backdrop: #d3d3d6;
    --paper: #f7f7f7;
    --brand-blue: #1746a8;
    --brand-blue-deep: #123a8c;
    --accent-gold: #e8b92e;
    --ink: #2a2f3a;
    --sky-top: #6f9fd6;
    --sky-mid: #a9c6e6;
    --stone: #8c8a86;
  }
  * { margin: 0; padding: 0; box-sizing: border-box; }
  html, body {
    width: 1200px; height: 840px; overflow: hidden;
    background: var(--backdrop);
  }
  .canvas {
    position: relative; width: 1200px; height: 840px;
    display: flex; align-items: center; justify-content: center;
  }
  .cover {
    position: relative; width: 600px; height: 760px;
    background: var(--paper);
    box-shadow: 0 18px 40px rgba(0,0,0,0.18);
    overflow: hidden;
  }
  .brand {
    position: absolute; top: 44px; right: 58px;
    display: flex; align-items: center; gap: 12px;
  }
  .brand-square {
    width: 30px; height: 30px; background: var(--brand-blue);
  }
  .brand-name {
    font-family: "Cinzel", serif; font-weight: 500;
    font-size: 46px; letter-spacing: 2px; color: var(--brand-blue);
    line-height: 1;
  }
  .brand-rule {
    position: absolute; top: 100px; right: 58px;
    width: 210px; height: 3px; background: var(--accent-gold);
  }
  .gold-rule {
    position: absolute; top: 114px; left: 60px;
    width: 372px; height: 3px; background: var(--accent-gold);
  }
  .hero-photo {
    position: absolute; top: 124px; left: 52px; right: 0; height: 420px;
    background: linear-gradient(160deg, var(--sky-top) 0%, var(--sky-mid) 38%, #4f6f9c 62%, var(--stone) 100%);
  }
  .title-panel {
    position: absolute; top: 494px; left: 60px;
    width: 400px; height: 182px;
    background: var(--brand-blue);
    padding: 30px 30px 0 48px;
    color: #fff;
  }
  .title-panel::before {
    content: ""; position: absolute; left: 28px; top: 34px;
    width: 2px; height: 112px; background: var(--accent-gold);
  }
  .title-brand {
    font-family: "Montserrat", sans-serif; font-weight: 700;
    font-size: 30px; letter-spacing: 2px; line-height: 1.1;
  }
  .title-text {
    margin-top: 8px;
    font-family: "Montserrat", sans-serif; font-weight: 700;
    font-size: 33px; line-height: 1.12; letter-spacing: 2px;
    text-transform: uppercase;
  }
  .side-rule {
    position: absolute; right: 22px; top: 620px;
    width: 2px; height: 58px; background: var(--accent-gold);
  }
  .website {
    position: absolute; right: 42px; bottom: 34px;
    font-family: "Montserrat", sans-serif; font-weight: 400;
    font-size: 15px; color: var(--ink); letter-spacing: 0.3px;
  }
  .website strong { color: var(--brand-blue); font-weight: 600; }
</style>
</head>
<body>
  <main class="canvas">
    <section class="cover">
      <div class="brand">
        <span class="brand-square"></span>
        <span class="brand-name">ORVANE</span>
      </div>
      <div class="brand-rule"></div>
      <div class="gold-rule"></div>

      <div class="hero-photo" role="img" aria-label="Upward view of city office towers, a glass skyscraper and a stone building against a blue sky"></div>

      <div class="title-panel">
        <div class="title-brand">ORVANE</div>
        <h1 class="title-text">Asset Tracing<br>Services</h1>
      </div>

      <div class="side-rule"></div>
      <p class="website">www.<strong>orvane</strong>.co.uk</p>
    </section>
  </main>
</body>
</html>
```